Brochure Design

I need a brochure that I can give to prospective clients during meetings and shows. My company website is www.brightpathmarketingpro.com

There is information to help with the creation of the brochure. Additionally, I will be attaching the new company logo. The website is being fixed behind the scenes to incorporate the new logo and color schemes. Please allow the colors in the brochure to the logo and not the current website.

Thanks!

```html
<!DOCTYPE html>
<html lang="en">
<head>
<meta charset="utf-8">
<title>Brightpath Trifold Brochure</title>
<link href="https://fonts.googleapis.com/css2?family=Open+Sans:ital,wght@0,400;0,600;1,400;1,600&display=swap" rel="stylesheet">
<style>
  :root {
    --page-bg: #e9e6e2;
    --lime: #8cc63f;
    --lime-light: #9ed14a;
    --mid-green-top: #6aa534;
    --mid-green-bottom: #3f7a1f;
    --band-green: #2e5c14;
    --band-green-dark: #244a0f;
    --title-green: #2c4a12;
    --body-green: #3f5f1f;
    --card-top: #ffffff;
    --card-bottom: #dcdcdc;
    --white: #ffffff;
  }
  * { box-sizing: border-box; margin: 0; padding: 0; }
  html, body { width: 1200px; height: 960px; overflow: hidden; }
  body {
    background: var(--page-bg);
    font-family: "Open Sans", Arial, sans-serif;
    position: relative;
  }
  .brochure {
    position: absolute;
    left: 30px; top: 40px;
    width: 1140px; height: 880px;
    display: flex;
    box-shadow: 0 8px 24px rgba(0,0,0,.25);
  }
  .panel {
    position: relative;
    width: 380px; height: 100%;
    background: linear-gradient(180deg, var(--lime-light), var(--lime));
    padding: 18px 16px 0;
  }
  .panel--center {
    background: linear-gradient(180deg, var(--mid-green-top) 0%, var(--mid-green-bottom) 100%);
    box-shadow: inset 6px 0 10px rgba(0,0,0,.12), inset -6px 0 10px rgba(0,0,0,.12);
  }
  .card {
    position: relative;
    height: 300px;
    border-radius: 8px;
    background: linear-gradient(180deg, var(--card-top), var(--card-bottom));
    box-shadow: 0 2px 4px rgba(0,0,0,.25);
    display: flex; flex-direction: column; align-items: center;
    padding-top: 18px;
  }
  .card::after {
    content: "";
    position: absolute; left: 50%; bottom: -9px;
    width: 16px; height: 16px;
    background: var(--card-bottom);
    transform: translateX(-50%) rotate(45deg);
    box-shadow: 2px 2px 2px rgba(0,0,0,.15);
  }
  .card__art {
    width: 190px; height: 190px;
    border-radius: 12px;
  }
  .art--media { background: radial-gradient(circle at 50% 55%, #c99a5a, #e2e2e2 70%); }
  .art--seo { background: radial-gradient(circle at 50% 45%, #e8822a, #bdbdbd 55%, #e4e4e4 75%); }
  .art--blend { width: 320px; background: linear-gradient(90deg, #e6e6e6, #3fa33a 30%, #f0c22a 65%, #e6e6e6); }
  .card__title {
    margin-top: 34px;
    font-weight: 600; font-size: 20px;
    color: var(--title-green);
    text-transform: uppercase;
    white-space: nowrap;
    text-align: center;
  }
  .panel__body { padding: 32px 14px 0; }
  .tagline {
    font-style: italic; font-weight: 600;
    font-size: 18px; line-height: 1.3;
    color: var(--title-green);
    margin-bottom: 26px;
  }
  .copy {
    font-size: 13px; line-height: 1.5;
    color: var(--body-green);
    margin-bottom: 14px;
  }
  .panel--center .copy { color: var(--white); }
  .panel--center .panel__body { padding-top: 110px; }
  .panel--right .panel__body { padding-top: 70px; }
  .url-band {
    position: absolute; left: 0; right: 0; bottom: 0;
    height: 80px;
    background: linear-gradient(180deg, var(--band-green), var(--band-green-dark));
    display: flex; align-items: center;
    padding-left: 28px;
  }
  .panel--center .url-band { background: linear-gradient(180deg, #2f6315, var(--band-green-dark)); }
  .panel--right .url-band { background: linear-gradient(180deg, #3f7a1f, var(--band-green)); }
  .url {
    color: #cfe6b0;
    font-size: 14px; letter-spacing: 3px;
  }
  .brand {
    position: absolute; right: 26px; bottom: 92px;
    display: flex; flex-direction: column; align-items: center; gap: 6px;
  }
  .brand__dot {
    width: 44px; height: 44px; border-radius: 50%;
    background: var(--band-green);
  }
  .brand__name {
    font-size: 18px; font-weight: 400;
    letter-spacing: 4px;
    color: var(--band-green);
  }
</style>
</head>
<body>
  <main class="brochure">
    <section class="panel panel--left">
      <div class="card">
        <div class="card__art art--media" role="img" aria-label="Illustration of an open delivery box filled with digital media icons"></div>
        <h2 class="card__title">Digital Media Marketing</h2>
      </div>
      <div class="panel__body">
        <p class="tagline">“Strategies focused on increasing the Reach and Visibility of your Business”</p>
        <p class="copy">There are many different ways a company can implement Digital Marketing and Social Media into their business strategy. It takes knowledge and experience in both of these areas to create a truly effective approach that will maximize available resources and grow a strong digital presence.</p>
        <p class="copy">At Brightpath, we can help your business to define and implement the best Digital Marketing and Social Media strategy in order to achieve your company's organizational goals.</p>
        <p class="copy">Contact Brightpath to schedule a complimentary consultation in order to learn more about how a Digital Marketing and Social Media strategy will benefit your company.</p>
      </div>
      <div class="url-band"><span class="url">www.brightpathmarketingpro.com</span></div>
    </section>

    <section class="panel panel--center">
      <div class="card">
        <div class="card__art art--seo" role="img" aria-label="3D illustration of the letters SEO beneath a globe ringed with search engine names"></div>
        <h2 class="card__title">Search Engine Optimization</h2>
      </div>
      <div class="panel__body">
        <p class="copy">There is more to internet popularity than just social. Search Engine Optimization and Search Engine Marketing are two additional pieces that will be needed in order to become ranked higher in search engine results and attract more traffic to your website.</p>
        <p class="copy">We can show you how to use your existing digital presence with an SEO and SEM strategy to rank higher in search results and reach even more potential customers.</p>
        <p class="copy">Contact Brightpath to schedule a complimentary consultation in order to learn more about how a Search Engine Optimization and Search Engine Marketing strategy will benefit your company.</p>
      </div>
      <div class="url-band"></div>
    </section>

    <section class="panel panel--right">
      <div class="card">
        <div class="card__art art--blend" role="img" aria-label="Illustration of two figures joining green and yellow puzzle pieces"></div>
        <h2 class="card__title">Blended Services</h2>
      </div>
      <div class="panel__body">
        <p class="copy">Truthfully, there are so many great things that we can do for your business in regards to increasing the organization's digital footprint and search engine ranking. We usually recommend that a business gives us a little bit of time to look at both of our service offerings. One just works so much better with the other, so why not experience the power of both? Even companies with existing social media efforts see a boost after we start incorporating our knowledge with your organizational goals.</p>
        <p class="copy">Contact Brightpath to schedule a complimentary consultation in order to learn more about how a blend of Digital Marketing, Social Media, SEO and SEM Strategy will benefit your company.</p>
      </div>
      <div class="brand">
        <span class="brand__dot"></span>
        <span class="brand__name">BRIGHTPATH</span>
      </div>
      <div class="url-band"></div>
    </section>
  </main>
</body>
</html>
```